Poster advertising a workshop on digital analytics

Poster to market a workshop I'm presenting. I work in digital analytics and my workshop will talk about how analytics used to be done and what's changed. People will be able to go to heaps of different workshops so I need a poster to make mine stand out.

Attachments:
* Poster copy to use.
* Two headshots you can use, select the one that best fits your design.
* Company logo
* Example of the poster wall from last years' conference, to give you an idea.

Poster specs:
A2 size at a portrait orientation
420mm x 594mm
5mm Bleed with Crop Marks
CMYK

Target Market(s)

Marketers

Industry/Entity Type

Marketing

Font styles to use
Serif
Sans Serif

Colors

Designer to choose colors to be used in the design.

Requirements
Must have
• Eye catching

```html
<!DOCTYPE html>
<html lang="en">
<head>
<meta charset="utf-8">
<title>Analytics Has Changed, Have You? — Workshop Poster</title>
<link rel="stylesheet" href="https://fonts.googleapis.com/css2?family=Bebas+Neue&family=Exo+2:ital,wght@0,300;0,400;0,700;1,700;1,800&display=swap">
<style>
  :root {
    --sky-light: #e6f0f8;
    --sky-mid: #bcd6ea;
    --sky-deep: #9fc2de;
    --lime: #d5e000;
    --leaf: #3ea83a;
    --azure: #1790df;
    --ink: #1e1e1e;
    --logo-blue: #1da1e6;
    --white: #ffffff;
    --portrait-tone: #c9b6a6;
  }
  * { margin: 0; padding: 0; box-sizing: border-box; }
  html, body { width: 902px; height: 1200px; overflow: hidden; background: var(--sky-light); }
  .poster {
    position: relative;
    width: 902px;
    height: 1200px;
    overflow: hidden;
    font-family: "Exo 2", "Helvetica Neue", Arial, sans-serif;
    color: var(--ink);
  }
  .poster-backdrop {
    position: absolute; inset: 0;
    background:
      linear-gradient(130deg, rgba(255,255,255,0.55) 0%, rgba(255,255,255,0) 40%),
      linear-gradient(220deg, var(--sky-mid) 0%, var(--sky-light) 45%, var(--sky-mid) 75%, var(--sky-deep) 100%);
  }
  .shapes { position: absolute; inset: 0; }
  .headline {
    position: absolute;
    font-family: "Bebas Neue", "Oswald", Impact, sans-serif;
    font-weight: 400;
    color: var(--ink);
    line-height: 0.76;
    letter-spacing: 2px;
  }
  .headline-statement { left: 66px; top: 118px; font-size: 136px; }
  .headline-question { right: 138px; top: 425px; font-size: 136px; text-align: right; }
  .section-title {
    font-weight: 800;
    font-style: italic;
    font-size: 27px;
    line-height: 1;
  }
  .intro { position: absolute; left: 44px; top: 510px; width: 450px; }
  .intro p {
    font-weight: 400;
    font-size: 19.5px;
    line-height: 1.3;
    margin-top: 4px;
  }
  .intro .intro-lead { width: 390px; }
  .intro p + p { margin-top: 12px; }
  .topics { position: absolute; left: 522px; top: 695px; width: 360px; }
  .topic-list { list-style: none; margin-top: 14px; }
  .topic-list li {
    position: relative;
    padding-left: 28px;
    font-size: 19.5px;
    line-height: 1.3;
    margin-bottom: 11px;
  }
  .topic-list li::before {
    content: "";
    position: absolute; left: 2px; top: 7px;
    width: 12px; height: 12px; border-radius: 50%;
    background: var(--azure);
  }
  .presenter-portrait {
    position: absolute;
    left: 48px; top: 830px;
    width: 156px; height: 156px;
    border-radius: 50%;
    border: 7px solid var(--white);
    background: radial-gradient(circle at 50% 40%, var(--portrait-tone) 0%, #a8cfc0 70%, #8fc4ae 100%);
  }
  .presenter { position: absolute; left: 50px; top: 996px; width: 460px; }
  .presenter p {
    font-size: 18.5px;
    line-height: 1.3;
    margin-top: 10px;
  }
  .presenter strong { font-weight: 700; }
  .brand {
    position: absolute;
    left: 512px; top: 1066px;
    display: flex; align-items: center; gap: 14px;
  }
  .brand-dot { width: 22px; height: 22px; border-radius: 50%; background: var(--logo-blue); }
  .brand-name {
    font-weight: 700;
    font-size: 38px;
    line-height: 1;
    color: var(--logo-blue);
    letter-spacing: 0.5px;
  }
</style>
</head>
<body>
<main class="poster">
  <div class="poster-backdrop" role="img" aria-label="Faceted light blue background scattered with faint outline icons of devices, charts, mail and settings"></div>

  <svg class="shapes" width="902" height="1200" viewBox="0 0 902 1200" aria-hidden="true">
    <defs>
      <clipPath id="clip-lime-disc"><circle cx="371" cy="195" r="335"/></clipPath>
      <clipPath id="clip-corner-disc"><circle cx="30" cy="1060" r="190"/></clipPath>
    </defs>
    <circle cx="371" cy="195" r="335" fill="var(--lime)" opacity="0.92"/>
    <circle cx="559" cy="500" r="195" fill="var(--azure)"/>
    <circle cx="559" cy="500" r="195" fill="var(--leaf)" clip-path="url(#clip-lime-disc)"/>
    <circle cx="30" cy="1060" r="190" fill="var(--lime)" opacity="0.92"/>
    <circle cx="205" cy="908" r="80" fill="var(--azure)"/>
    <circle cx="205" cy="908" r="80" fill="var(--leaf)" clip-path="url(#clip-corner-disc)"/>
  </svg>

  <h1 class="headline headline-statement">Analytics<br>has changed,</h1>
  <p class="headline headline-question">Have<br>you?</p>

  <section class="intro">
    <h2 class="section-title">Analytics</h2>
    <p class="intro-lead">Isn't the afterthought it once was, but has rapidly become the driver of digital businesses. Tools have got more sophisticated and practices have improved the reliability and breadth of what's recorded.</p>
    <p>Is your business still stuck doing it the 1990s way, and what can you do about it? Owen walks through the evolution of digital analytics, how to do things properly today and where things are headed.</p>
  </section>

  <section class="topics">
    <h2 class="section-title">We'll cover</h2>
    <ul class="topic-list">
      <li>Not your grandmother's<br>Digital Analytics</li>
      <li>Tag management to move fast</li>
      <li>Data assurance to prevent breaking things</li>
      <li>Tool improvements and changes</li>
      <li>How to get to the new world of modern digital analytics</li>
    </ul>
  </section>

  <div class="presenter-portrait" role="img" aria-label="Headshot photo of the presenter"></div>

  <section class="presenter">
    <h2 class="section-title">The presenter</h2>
    <p><strong>Owen Fairlie</strong> has been doing Internet stuff for 25 years and got into digital analytics while trying to understand what people were doing on web sites and why. He loves joining the dots between different sets of data in order to tell a story.</p>
  </section>

  <div class="brand">
    <span class="brand-dot"></span>
    <span class="brand-name">Frostline Analytics</span>
  </div>
</main>
</body>
</html>
```